Eye catching Stationary Design

Healthcare consultant firm looking for stationary design ( letterhead, envelope and business cards) That’s professional, classy and eye catching . The design should incorporate the logo and the colors of the logo in its design. You can see the logo on our website at www crestmore advisory. net.

```html
<!DOCTYPE html>
<html lang="en">
<head>
<meta charset="utf-8">
<title>Crestmore Advisory – Business Cards</title>
<link rel="stylesheet" href="https://fonts.googleapis.com/css2?family=Cinzel:wght@400&family=Montserrat:wght@500;700&display=swap">
<style>
  :root {
    --bg: #3a3b3e;
    --sky: #29a8d9;
    --navy: #0a57a8;
    --ink: #060708;
    --photo-dark: #1c1d20;
    --white: #ffffff;
    --text-dark: #111418;
  }
  * { box-sizing: border-box; margin: 0; padding: 0; }
  html, body { width: 1200px; height: 900px; overflow: hidden; }
  body {
    background: var(--bg);
    font-family: "Montserrat", sans-serif;
    position: relative;
  }
  .card {
    position: absolute;
    width: 560px;
    height: 320px;
    overflow: hidden;
    box-shadow: 0 14px 30px rgba(0,0,0,.45);
  }
  .card-shapes { position: absolute; inset: 0; }
  .card--front { left: 60px; top: 90px; }
  .card--back { left: 580px; top: 490px; }

  .brand {
    position: absolute;
    display: flex;
    align-items: center;
    gap: 10px;
    font-family: "Cinzel", serif;
    font-weight: 400;
    color: var(--white);
    white-space: nowrap;
  }
  .brand-dot {
    width: 14px; height: 14px; border-radius: 50%;
    background: var(--sky);
    flex: none;
  }
  .card--front .brand { left: 150px; top: 92px; font-size: 21px; letter-spacing: 1px; }
  .card--back .brand { left: 36px; top: 146px; font-size: 17px; letter-spacing: .8px; }

  .front-links {
    position: absolute;
    left: 0; right: 0; top: 212px;
    text-align: center;
    color: var(--white);
    font-weight: 500;
  }
  .front-links .web { font-size: 13px; display: flex; justify-content: center; align-items: center; gap: 8px; }
  .front-links .mail { font-size: 14px; margin-top: 22px; }

  .icon {
    width: 18px; height: 18px; border-radius: 50%;
    background: var(--white);
    display: inline-flex; align-items: center; justify-content: center;
    flex: none;
  }

  .person { position: absolute; left: 356px; top: 58px; }
  .person-name { color: var(--white); font-weight: 700; font-size: 22px; letter-spacing: .5px; }
  .person-role { color: var(--navy); font-weight: 700; font-size: 16px; letter-spacing: .5px; margin-top: 2px; }

  .contacts { position: absolute; left: 350px; top: 148px; list-style: none; }
  .contacts li {
    display: flex; align-items: flex-start; gap: 9px;
    color: var(--text-dark); font-weight: 500; font-size: 11.5px;
    line-height: 1.35; margin-bottom: 10px;
  }
</style>
</head>
<body>

  <section class="card card--front" aria-label="Business card front">
    <svg class="card-shapes" viewBox="0 0 560 320" width="560" height="320">
      <rect width="560" height="320" fill="var(--sky)"/>
      <path d="M0 0 H560 V120 Q330 262 0 262 Z" fill="var(--navy)"/>
      <path d="M0 0 H560 V112 Q330 254 0 254 Z" fill="var(--photo-dark)" role="img" aria-label="Darkened photo of a healthcare team meeting"/>
    </svg>
    <div class="brand"><span class="brand-dot"></span>Crestmore Advisory LLC</div>
    <div class="front-links">
      <div class="web">
        <span class="icon">
          <svg width="12" height="12" viewBox="0 0 12 12" fill="none" stroke="var(--navy)" stroke-width="1"><circle cx="6" cy="6" r="5"/><ellipse cx="6" cy="6" rx="2.2" ry="5"/><path d="M1 6h10M2 3.5h8M2 8.5h8"/></svg>
        </span>
        crestmoreadvisory.net
      </div>
      <div class="mail">info@crestmoreadvisory.net</div>
    </div>
  </section>

  <section class="card card--back" aria-label="Business card back">
    <svg class="card-shapes" viewBox="0 0 560 320" width="560" height="320">
      <rect width="560" height="320" fill="var(--sky)"/>
      <path d="M0 0 H200 Q370 70 352 320 H0 Z" fill="var(--navy)"/>
      <path d="M0 0 H180 Q350 80 334 320 H0 Z" fill="var(--ink)"/>
    </svg>
    <div class="brand"><span class="brand-dot"></span>Crestmore Advisory LLC</div>
    <div class="person">
      <div class="person-name">MARCUS HALE</div>
      <div class="person-role">DIRECTOR</div>
    </div>
    <ul class="contacts">
      <li>
        <span class="icon"><svg width="11" height="11" viewBox="0 0 12 12" fill="var(--navy)"><path d="M3 1.5l2 2.2-1.2 1.3a6 6 0 003.2 3.2L8.3 7l2.2 2-1.3 1.8C5.5 10.6 1.4 6.5 1.2 2.8z"/></svg></span>
        <span>(555) 214-0387</span>
      </li>
      <li>
        <span class="icon"><svg width="12" height="12" viewBox="0 0 12 12" fill="none" stroke="var(--navy)" stroke-width="1"><circle cx="6" cy="6" r="5"/><ellipse cx="6" cy="6" rx="2.2" ry="5"/><path d="M1 6h10M2 3.5h8M2 8.5h8"/></svg></span>
        <span>info@crestmoreadvisory.net</span>
      </li>
      <li>
        <span class="icon"><svg width="10" height="12" viewBox="0 0 10 12" fill="var(--navy)"><path d="M5 0.5a4 4 0 014 4c0 3-4 7-4 7s-4-4-4-7a4 4 0 014-4zm0 2.4a1.6 1.6 0 100 3.2 1.6 1.6 0 000-3.2z"/></svg></span>
        <span>118 Linden St Suite 40,<br>Riverton, NY 10120, USA</span>
      </li>
    </ul>
  </section>

</body>
</html>
```